Business card for wedding & event planning company

I'm looking for a well designed double sided business card to represent my wedding and event planning company.

It should include the fact we manage the following events:
Weddings, birthdays, conferences, product launches, fashion shows & conventions
in the following areas:
Wiltshire, Oxfordshire, Berkshire & London

My contact details to be included are:

Moira Pennock
07715 482036
moira@amberlarkcelebrations.co.uk
www.amberlarkcelebrations.co.uk

My logo can be found at the following Filevaultex location:
AI file: https://www.filevaultex.com/s/k4mprt8wn31b7hz/brandlogo_sourcefile.ai?dl=0
PNG file:
https://www.filevaultex.com/s/h9qsle2vbx07mnd/brandlogo_image.png?dl=0

Target Market(s)

women aged 30-55

Industry/Entity Type

Wedding

Contact Information for Business Card

in the following areas:

Moira Pennock
Event Planner
07715 482036

Font styles to use
Serif
Sans Serif
Script

Requirements
Must have
• Purple and white colour scheme
Should not have
• Black background
• Please don't submit any of the see-through business card designs.

```html
<!DOCTYPE html>
<html lang="en">
<head>
<meta charset="utf-8">
<title>Amber Lark Celebrations – Business Card</title>
<link rel="stylesheet" href="https://fonts.googleapis.com/css2?family=Open+Sans:wght@400;600;700&display=swap">
<style>
  :root {
    --purple: #8b3a9c;
    --purple-deep: #7a2f8a;
    --black: #0d0d0d;
    --white: #ffffff;
    --ink: #1a1a1a;
    --backdrop: #ecebee;
  }
  * { box-sizing: border-box; margin: 0; padding: 0; }
  html, body {
    width: 1200px; height: 1200px; overflow: hidden;
    background: var(--backdrop);
    font-family: "Open Sans", Arial, sans-serif;
  }
  .canvas {
    width: 1200px; height: 1200px;
    display: flex; flex-direction: column; align-items: center; justify-content: center;
    gap: 60px;
  }
  .card {
    position: relative;
    width: 860px; height: 500px;
    border-radius: 6px;
    overflow: hidden;
    box-shadow: 0 10px 28px rgba(0,0,0,0.16);
  }

  /* Back */
  .card-back {
    background:
      repeating-linear-gradient(180deg, rgba(255,255,255,0.035) 0 2px, rgba(0,0,0,0.035) 2px 4px),
      var(--purple);
    color: var(--white);
    display: flex; flex-direction: column; align-items: center; justify-content: center;
    text-align: center;
  }
  .card-back .faint-mark {
    position: absolute; left: 50%; top: 50%;
    width: 330px; height: 330px; margin: -165px 0 0 -165px;
    border-radius: 50%;
    border: 2px solid rgba(255,255,255,0.09);
  }
  .service-heading {
    position: relative;
    font-weight: 700; font-size: 24px; letter-spacing: 0.5px;
    margin-bottom: 4px;
  }
  .service-list {
    position: relative;
    font-weight: 400; font-size: 22px; line-height: 1.4; letter-spacing: 0.8px;
  }
  .service-list + .service-heading { margin-top: 22px; }

  /* Front */
  .card-front { background: var(--white); }
  .card-front svg.bands { position: absolute; inset: 0; }
  .holder-name {
    position: absolute; left: 96px; top: 28px;
    font-weight: 700; font-size: 30px; color: var(--purple);
  }
  .contact {
    position: absolute; left: 40px; top: 238px;
    list-style: none;
    font-size: 22px; line-height: 36px; color: var(--ink);
  }
  .contact .label { color: var(--purple); font-weight: 600; display: inline-block; width: 30px; }
  .brand {
    position: absolute; left: 470px; top: 225px;
    display: flex; align-items: center; gap: 16px;
  }
  .brand-dot { width: 58px; height: 58px; border-radius: 50%; border: 3px solid var(--purple); }
  .brand-name {
    font-weight: 600; font-size: 30px; color: var(--purple); line-height: 1.15;
  }
</style>
</head>
<body>
<main class="canvas">

  <section class="card card-back" aria-label="Card back: services and areas">
    <div class="faint-mark" aria-hidden="true"></div>
    <h2 class="service-heading">EVENTS</h2>
    <p class="service-list">WEDDINGS | BIRTHDAYS | CONFERENCES |<br>PRODUCT LAUNCHES | FASHION SHOWS</p>
    <h2 class="service-heading">CONVENTION AREAS</h2>
    <p class="service-list">WILTSHIRE | OXFORDSHIRE | BERKSHIRE | LONDON</p>
  </section>

  <section class="card card-front" aria-label="Card front: contact details">
    <svg class="bands" width="860" height="500" viewBox="0 0 860 500" aria-hidden="true">
      <polygon points="0,28 46,28 30,70 0,70" fill="var(--purple)"/>
      <polygon points="52,28 84,28 68,70 36,70" fill="var(--black)"/>
      <polygon points="0,372 430,372 462,408 0,408" fill="var(--purple)"/>
      <polygon points="462,408 860,408 860,452 500,452" fill="var(--black)"/>
      <polygon points="430,372 860,372 860,408 462,408" fill="var(--white)"/>
    </svg>
    <h1 class="holder-name">Moira Pennock</h1>
    <ul class="contact">
      <li><span class="label">T:</span>07715 482036</li>
      <li><span class="label">E:</span>moira@amberlarkcelebrations.co.uk</li>
      <li><span class="label">W:</span>www.amberlarkcelebrations.co.uk</li>
    </ul>
    <div class="brand">
      <span class="brand-dot" aria-hidden="true"></span>
      <span class="brand-name">Amber Lark<br>Celebrations</span>
    </div>
  </section>

</main>
</body>
</html>
```